Label Design for American Pet Health Startup

We need your help in creating a line-up of labels for our upcoming products. The products will come in two different sizes/shapes. We have a logo (sourced form ArtSquadron!) to start from and a pretty extensive brief (see attached.) The winning design will be bold, simple, and create a strongly branded look to the whole line while allowing consumers to easily sort through the different SKUs.

The logo and other existing design elements are in the attached powerpoint. I will also post some of the source files.

If you choose to compete for this project, please read the creative brief and the powerpoint very carefully before starting.

Thank you for your time and consideration.

Target Market(s)

Pet owners (dog owners, initially) who care deeply about their pets. Their pets are older and may not be thriving the way they once were. The owners want their pets to have the highest quality of life possible, for as long as is practical. They take their pets frequently to the vet and have great faith in veterinary medicine, but they also believe that dietary supplements may have a beneficial effect. They believe this to be possible because they take supplements themselves.

They are probably older--empty nesters or soon to be. They’ve owned their dog for five years or more, or have rescued an older dog from a shelter. Their dog is, in many ways, a full member of their family.

Industry/Entity Type

Pet Care

Font styles to use
Sans Serif

Requirements
Must have
• Please see the attached brief for this detail. I have cut and paste it into this form but it doesn't translate well. Reading the Word document will be easier and the links will work.
• Packaging Creative Considerations: The product packaging needs to . . .
• • Have a strong, branded line look.
• - The logo has already been developed, and I would like you to be guided in your design choices by its structure and color, but I am open to deviations from the existing work if it leads to a strong design
• • Use color or some other design elements to distinguish each SKU from the other
• • Be bold and simple. This product will typically be merchandised online, with very small images of the packaging. Simple and bold design elements will ensure that the products are both noticed and understood.
• - The product will likely be contained within white plastic or aluminum (silver) bottles with white caps/pumps. However, if you believe your design concepts would benefit from a particular color of bottle/container, please illustrate that, as that would be possible to execute.
• • Communicate that these products are for pets without using any clichés. This category is full of packaging with stock photos of dogs and cats. Please avoid this at all costs. Instead, please unleash your creativity to illustrate the products’ nature/purposes.
• A couple of packaging designs I would like you to draw inspiration from:
• o Vemo. This line is for human supplements/vitamins. Notice the strong line look, the simple and bold graphics, and the smart use of color and other design elements to differentiate the SKUs (while still holding it together as a single brand.)
• o Tupka. This line is for pets. Again, notice the strong line look, the smart use of color to differentiate the SKUs, and the simple and bold presentation that translates so well on the screen.
• o Crumblefin. This design is not as good as the first two, but it does accomplish several of the brief’s objectives and the packaging is likely to be very similar to what your design will eventually be affixed to.
• Design Deliverables: A great submission will illustrate its strength by showing how the design translates across all the expected SKUs. To accomplish, this, I would recommend using the “functional maps” I’ve included in the attached Powerpoint document to:
• o First illustrate, in greater size and detail, one SKU each of the two families (one oil SKU and one supplement SKU)
• o Then illustrate how each of those designs extends across the rest of the family. That illustration can be less detailed. We just need to see how the colors and other design elements extend.
Should not have
• No stock images of cats or dogs; please avoid junking up the designs with too many elements

```html
<!DOCTYPE html>
<html lang="en">
<head>
<meta charset="utf-8">
<title>Wagwell Oil Supplement Labels</title>
<link rel="stylesheet" href="https://fonts.googleapis.com/css2?family=Montserrat:wght@500;600;700&family=Quicksand:wght@500&display=swap">
<style>
  :root {
    --canvas: #f1f2f3;
    --label: #ffffff;
    --ink: #111111;
    --muted: #8a8a8a;
    --teal: #16a9b9;
    --paw: #1fa8bc;
    --salmon: #ef4a2c;
    --salmon-light: #f47152;
    --aqua: #25b3b3;
    --aqua-light: #6cd2cd;
    --dot: #8c8c8c;
  }
  * { box-sizing: border-box; margin: 0; padding: 0; }
  html, body { width: 1200px; height: 1040px; overflow: hidden; }
  body {
    background: var(--canvas);
    font-family: "Montserrat", sans-serif;
    position: relative;
  }
  .label {
    position: absolute;
    top: 110px;
    width: 360px;
    height: 820px;
    background: var(--label);
    border-radius: 14px;
    box-shadow: 0 2px 10px rgba(0,0,0,0.08);
    display: flex;
    flex-direction: column;
    align-items: center;
    text-align: center;
  }
  .label--salmon { left: 180px; }
  .label--omega { left: 660px; }

  .brand {
    margin-top: 74px;
    display: flex;
    align-items: center;
    gap: 10px;
    font-family: "Quicksand", sans-serif;
    font-weight: 500;
    font-size: 40px;
    color: var(--teal);
    letter-spacing: 0.5px;
  }
  .brand__dot {
    width: 16px; height: 16px;
    border-radius: 50%;
    background: var(--teal);
  }

  .product { margin-top: 44px; height: 92px; display: flex; flex-direction: column; justify-content: center; color: var(--ink); }
  .product__small { font-weight: 700; font-size: 19px; letter-spacing: 1px; }
  .product__large { font-weight: 600; font-size: 40px; letter-spacing: 1.5px; line-height: 1.1; }

  .benefit { margin-top: 6px; font-weight: 500; font-size: 17px; color: var(--muted); letter-spacing: 0.3px; }

  .visual { margin-top: 20px; position: relative; width: 240px; height: 132px; }
  .paws { position: absolute; width: 58px; height: 68px; border-radius: 6px; background: var(--paw); }
  .paws--left { left: 0; top: 2px; }
  .paws--right { right: 0; top: 56px; }
  .drop-area { position: absolute; left: 73px; top: 0; width: 94px; height: 128px; border-radius: 8px; }
  .drop-area--salmon { background: linear-gradient(135deg, var(--salmon-light), var(--salmon)); }
  .drop-area--omega { background: linear-gradient(135deg, var(--aqua-light), var(--aqua)); }

  .supplement { margin-top: 24px; font-weight: 500; font-size: 17px; color: var(--muted); }
  .audience { margin-top: 4px; font-weight: 600; font-size: 28px; color: var(--teal); letter-spacing: 0.5px; }

  .range { margin-top: 18px; display: flex; gap: 9px; }
  .range__dot { width: 14px; height: 14px; border-radius: 50%; background: var(--dot); }
  .range__dot--salmon { background: var(--salmon); }
  .range__dot--omega { background: var(--teal); }

  .origin {
    margin-top: 22px;
    border: 1px solid var(--ink);
    padding: 6px 14px;
    font-family: "Quicksand", sans-serif;
    font-weight: 500;
    font-size: 16px;
    line-height: 1.3;
    color: var(--ink);
  }
  .net { margin-top: 24px; font-weight: 500; font-size: 12px; color: var(--muted); letter-spacing: 0.5px; }
</style>
</head>
<body>

  <section class="label label--salmon">
    <div class="brand"><span class="brand__dot"></span>Wagwell</div>
    <div class="product">
      <p class="product__small">PURE</p>
      <p class="product__large">SALMON OIL</p>
    </div>
    <p class="benefit">Supports Healthy Coat &amp; Skin</p>
    <div class="visual">
      <div class="paws paws--left" role="img" aria-label="Cluster of four small teal paw prints"></div>
      <div class="drop-area drop-area--salmon" role="img" aria-label="Oil drop illustration filled with salmon flesh texture"></div>
      <div class="paws paws--right" role="img" aria-label="Cluster of four small teal paw prints"></div>
    </div>
    <p class="supplement">All Natural Supplement</p>
    <p class="audience">For Dogs + Cats</p>
    <div class="range">
      <span class="range__dot"></span><span class="range__dot"></span>
      <span class="range__dot range__dot--salmon"></span>
      <span class="range__dot"></span><span class="range__dot"></span>
    </div>
    <div class="origin">Made in USA<br>with 100%<br>Wild Alaskan Salmon</div>
    <p class="net">Net 32 FL OZ / 946 ML</p>
  </section>

  <section class="label label--omega">
    <div class="brand"><span class="brand__dot"></span>Wagwell</div>
    <div class="product">
      <p class="product__large">OMEGA 3</p>
      <p class="product__small">FISH OIL</p>
    </div>
    <p class="benefit">Supports Healthy Coat &amp; Skin</p>
    <div class="visual">
      <div class="paws paws--left" role="img" aria-label="Cluster of four small teal paw prints"></div>
      <div class="drop-area drop-area--omega" role="img" aria-label="Oil drop illustration filled with teal fish scale texture"></div>
      <div class="paws paws--right" role="img" aria-label="Cluster of four small teal paw prints"></div>
    </div>
    <p class="supplement">All Natural Supplement</p>
    <p class="audience">For Dogs + Cats</p>
    <div class="range">
      <span class="range__dot"></span><span class="range__dot"></span>
      <span class="range__dot range__dot--omega"></span>
      <span class="range__dot"></span><span class="range__dot"></span>
    </div>
    <div class="origin">Made in USA<br>with Atlantic Sardines<br>&amp; Anchovies</div>
    <p class="net">Net 32 FL OZ / 946 ML</p>
  </section>

</body>
</html>
```